Service business needs Business Card Design

Looking to create a new business card design that is both professional and unique the can highlight the many services we offer throughout the seasons. Our tagline is "The Steadfast Touch"
Licensed & Insured: PA392617 has to be small and on the back side of the card.
On the Front:
FirstName LastName
Title
We offer the following services:
Deck Repair and Maintenance
Deck Cleaning and Staining/Painting
Power Washing/House Washing
Landscape Lighting Installation
Christmas Lighting Installation

```html
<!DOCTYPE html>
<html lang="en">
<head>
<meta charset="utf-8">
<title>Northway Services – Business Card</title>
<link rel="stylesheet" href="https://fonts.googleapis.com/css2?family=Cabin:wght@600&family=Fira+Sans+Condensed:wght@500;600&display=swap">
<style>
  :root {
    --navy: #034b87;
    --sky: #0aa0e6;
    --paper: #ffffff;
    --card-edge: #d6e6ee;
    --licence-blue: #2a82c6;
    --logo-navy: #0d4c87;
  }
  html, body {
    margin: 0;
    padding: 0;
    width: 1025px;
    height: 1200px;
    overflow: hidden;
    background: var(--paper);
  }
  .canvas {
    position: relative;
    width: 1025px;
    height: 1200px;
  }
  .card {
    position: absolute;
    left: 28px;
    width: 969px;
    height: 554px;
    overflow: hidden;
  }
  .card--front {
    top: 32px;
    background: var(--navy);
    box-shadow: 0 0 0 1px var(--card-edge);
  }
  .card--back {
    top: 616px;
    height: 550px;
    background: var(--navy);
  }
  .front-shapes {
    position: absolute;
    inset: 0;
    width: 100%;
    height: 100%;
  }
  .brand {
    position: absolute;
    left: 30px;
    top: 250px;
    width: 350px;
    text-align: center;
    font-family: "Fira Sans Condensed", sans-serif;
    font-weight: 600;
    font-size: 44px;
    letter-spacing: 1px;
    color: var(--logo-navy);
    line-height: 1;
  }
  .contact {
    position: absolute;
    right: 43px;
    top: 48px;
    text-align: right;
    font-family: "Fira Sans Condensed", sans-serif;
    font-weight: 600;
    font-size: 28px;
    line-height: 37px;
    color: var(--paper);
  }
  .services {
    position: absolute;
    left: 443px;
    top: 332px;
    margin: 0;
    padding: 0;
    list-style: none;
    font-family: "Fira Sans Condensed", sans-serif;
    font-weight: 600;
    font-size: 27.5px;
    line-height: 37.5px;
    color: var(--paper);
    letter-spacing: 0.2px;
  }
  .services li {
    position: relative;
    padding-left: 19px;
  }
  .services li::before {
    content: "";
    position: absolute;
    left: 0;
    top: 14px;
    width: 8px;
    height: 8px;
    background: var(--paper);
  }
  .licence {
    position: absolute;
    left: 0;
    right: 0;
    top: 250px;
    text-align: center;
    font-family: "Cabin", sans-serif;
    font-weight: 600;
    font-size: 40px;
    line-height: 1;
    color: var(--licence-blue);
  }
</style>
</head>
<body>
<div class="canvas">
  <section class="card card--front">
    <svg class="front-shapes" viewBox="0 0 1050 600" preserveAspectRatio="none" aria-hidden="true">
      <polygon points="0,0 332,0 474,305 312,600 0,600" fill="var(--sky)"/>
      <polygon points="0,0 306,0 471,305 285,600 0,600" fill="var(--paper)"/>
    </svg>
    <div class="brand">Northway Services</div>
    <div class="contact">
      <div class="contact__name">First name Last name</div>
      <div class="contact__title">Title</div>
    </div>
    <ul class="services">
      <li>Deck Repair and Maintenance</li>
      <li>Deck Cleaning and Staining/Painting</li>
      <li>Christmas Lighting Installation</li>
      <li>Landscape Lighting Installation</li>
      <li>Power Washing/House Washing</li>
    </ul>
  </section>
  <section class="card card--back">
    <p class="licence">Licensed &amp; Insured: PA392617</p>
  </section>
</div>
</body>
</html>
```